Entrepreneur needs a business card design

I need a business card to name my three companies, as well as contact information.
I'm open on design and color and it can be plain or complex. I'm open on colors but I think I prefer something somewhat formal but fun as well.
I'm open on whether the background is plain or has design in it. I don't have company logos.
Target Market(s)
Auto dealers, realtors and property managers
Industry/Entity Type
Business
Contact Information for Business Card
HOLLISTER FAMILY PROPERTIES, LLC
HOLLISTER PUBLISHING, LLC
LOTMASTER CONSULTING, LLC
Ned Hollister
2847 W. Tamarack Ave. #310
Boise, Idaho 83611-2905
208-514-3092
ned@holl5x.example

```html
<!DOCTYPE html>
<html lang="en">
<head>
<meta charset="utf-8">
<title>Ned Hollister — Business Card</title>
<link rel="stylesheet" href="https://fonts.googleapis.com/css2?family=Merriweather:wght@700;900&family=PT+Sans:wght@400;700&family=PT+Serif:ital@1&display=swap">
<style>
  :root {
    --ink: #000000;
    --paper: #ffffff;
    --reverse-text: #f4f4f4;
    --body-text: #1e1e1e;
  }
  * { margin: 0; padding: 0; box-sizing: border-box; }
  html, body {
    width: 1200px;
    height: 764px;
    overflow: hidden;
    background: var(--paper);
  }
  .card {
    position: relative;
    width: 1200px;
    height: 764px;
    background: var(--paper);
  }
  .header-band {
    position: absolute;
    left: 0; top: 0;
    width: 1200px;
    height: 366px;
    background: var(--ink);
  }
  .owner-name {
    position: absolute;
    left: 186px;
    top: 56px;
    font-family: "Merriweather", Georgia, serif;
    font-weight: 900;
    font-size: 80px;
    letter-spacing: 6px;
    color: var(--reverse-text);
    white-space: nowrap;
  }
  .company {
    position: absolute;
    top: 238px;
    width: 360px;
    transform: translateX(-50%);
    text-align: center;
    font-size: 29px;
    line-height: 38px;
    letter-spacing: 1.5px;
    color: var(--reverse-text);
    text-transform: uppercase;
  }
  .company--serif {
    font-family: "Merriweather", Georgia, serif;
    font-weight: 700;
    font-size: 27px;
  }
  .company--sans {
    font-family: "PT Sans", Arial, sans-serif;
    font-weight: 700;
    letter-spacing: 2px;
  }
  .company--properties { left: 253px; }
  .company--publishing { left: 593px; }
  .company--consulting { left: 943px; }

  .contact {
    position: absolute;
    right: 102px;
    top: 470px;
    text-align: right;
    font-family: "PT Sans", Arial, sans-serif;
    font-size: 29px;
    letter-spacing: 4.5px;
    color: var(--body-text);
    list-style: none;
  }
  .contact li { line-height: 38px; }
  .contact li.gap-before { margin-top: 10px; }
  .contact .label {
    font-family: "PT Serif", Georgia, serif;
    font-style: italic;
    letter-spacing: 3px;
  }
</style>
</head>
<body>
  <div class="card">
    <header class="header-band">
      <h1 class="owner-name">Ned Hollister</h1>
      <p class="company company--serif company--properties">Hollister Family<br>Properties, LLC</p>
      <p class="company company--sans company--publishing">Hollister<br>Publishing, LLC</p>
      <p class="company company--serif company--consulting">Lotmaster<br>Consulting, LLC</p>
    </header>

    <ul class="contact">
      <li><span class="label">A:</span>2847 W.Tamarack Ave.</li>
      <li>#310 Boise, Idaho</li>
      <li class="gap-before"><span class="label">C:</span>83611-2905</li>
      <li><span class="label">C:</span>208-514-3092</li>
      <li><span class="label">E-add:</span>ned@holl5x.example</li>
    </ul>
  </div>
</body>
</html>
```